pinecrestharborway.org website

We need a website that is designed in part to look like our current website but even better. I have done the design work to this point and am limited on how to make word press work. I need it cleaned up and improved. I also need places for our ministry brands and products with a link to another part of the website where I can put the flyers I have that give a more complete description. The also need to be linked to our store to purchase products connected to that ministry.

Target Market(s)

Those who are looking for ways to grow their ministries to married couples.

Industry/Entity Type

Work

Number of Pages Required

5+ page

Colors
0355a3

Requirements
Must have
• I need a great front page with links to other pages on the website using the flyers I've attached as the content on the subsequent pages. There are pages already in place that need to remain. I can forward to you the admin passcode and password to take pages from our current website. You can see I like the dark blue and would like to have that color remain as a dominant factor in the layout.

```html
<!DOCTYPE html>
<html lang="en">
<head>
<meta charset="utf-8">
<title>Pinecrest Harborway</title>
<link href="https://fonts.googleapis.com/css2?family=Raleway:wght@400;500;600;700&family=Open+Sans:ital,wght@0,400;0,600;1,400&family=Shadows+Into+Light+Two&family=Reenie+Beanie&display=swap" rel="stylesheet">
<style>
:root{
  --blue:#0355a3;
  --navy:#0b3f80;
  --nav-top:#1a5ea8;
  --nav-bottom:#0a4388;
  --nav-active:#5a93b8;
  --teal:#6a98ae;
  --ink:#333333;
  --text:#6b6b6b;
  --soft:#f4f8fc;
  --line:#e2e2e2;
  --footer:#333333;
}
*{box-sizing:border-box;margin:0;padding:0}
html,body{width:1200px;height:2426px;overflow:hidden}
body{position:relative;background:#fff;font-family:"Open Sans",sans-serif;color:var(--text)}
.abs{position:absolute}

/* header */
.brand{left:99px;top:24px;width:300px}
.brand .tagline{font:italic 600 11px "Open Sans",sans-serif;color:var(--blue);margin-left:130px}
.brand .name{display:flex;align-items:center;gap:10px;margin-top:8px;white-space:nowrap}
.brand .mark{width:28px;height:28px;background:var(--navy);flex:none}
.brand .name span{font:700 21px "Raleway",sans-serif;color:var(--navy);letter-spacing:.2px}
.brand .sub{font:600 13px "Raleway",sans-serif;color:var(--navy);margin:2px 0 0 38px}
.brand .url{font:500 9px "Open Sans",sans-serif;color:var(--blue);margin:6px 0 0 140px}
.social{right:99px;top:58px;display:flex;align-items:center;gap:8px}
.social .search{width:30px;height:30px;border-radius:50%;background:#eef2f6;display:flex;align-items:center;justify-content:center;margin-right:14px}
.social .label{font:500 12px "Raleway",sans-serif;color:#777;margin-right:4px}
.social .dot{width:28px;height:28px;border-radius:50%}

/* nav */
.nav{left:0;top:145px;width:1200px;height:63px;background:linear-gradient(var(--nav-top),var(--nav-bottom));display:flex;padding-left:99px}
.nav a{display:flex;align-items:center;justify-content:center;height:63px;color:#fff;text-decoration:none;font:600 12px "Raleway",sans-serif;letter-spacing:.3px}
.nav a.active{background:var(--nav-active)}

/* hero */
.hero{left:0;top:208px;width:1200px;height:530px;background:linear-gradient(180deg,#6f93c4 0%,#b9c6d6 35%,#d9d6cc 62%,#7b9a4e 88%,#5b7a34 100%)}
.hero h1{position:absolute;left:100px;top:150px;font:400 58px/1.05 "Reenie Beanie",cursive;color:#fff;text-shadow:0 2px 4px rgba(0,0,0,.35)}
.arrow{position:absolute;top:215px;width:32px;height:32px;border-radius:50%;background:rgba(60,60,60,.55);display:flex;align-items:center;justify-content:center}
.mission{left:99px;top:679px;width:1002px;height:110px;background:var(--soft);box-shadow:0 10px 12px -8px rgba(0,0,0,.35);text-align:center;padding-top:22px;font:400 15px/1.7 "Shadows Into Light Two",cursive;color:var(--navy);white-space:nowrap}

/* sections */
.h2{font:700 24px "Raleway",sans-serif;color:#333;white-space:nowrap}
.welcome-img{left:100px;top:886px;width:293px;height:212px;background:#0f1b2b}
.body{font:400 11px/2.1 "Open Sans",sans-serif;color:#666}
.btn{display:flex;align-items:center;justify-content:center;width:116px;height:40px;border-radius:4px;background:linear-gradient(#0e5aa8,#073f7e);color:#fff;font:700 12px "Raleway",sans-serif;text-decoration:none}
.rule{height:1px;background:var(--line)}
.quote{left:99px;top:1216px;width:706px;height:123px;background:var(--teal);color:#fff;padding:16px 18px 0;font:400 13.5px/1.8 "Shadows Into Light Two",cursive}
.quote::after{content:"";position:absolute;left:60px;bottom:-12px;border:12px solid transparent;border-bottom:0;border-top-color:var(--teal)}
.quote .pager{position:absolute;right:20px;bottom:12px;display:flex;gap:5px}
.quote .pager i{width:9px;height:9px;border-radius:50%;background:rgba(255,255,255,.55)}
.badge{top:1355px;width:223px;height:118px;border:1px solid #dcdcdc;display:flex;align-items:center;justify-content:center}
.badge b{display:block;width:120px;height:58px;border-radius:6px}
.lead{left:99px;top:1538px;width:706px;font:700 14px "Raleway",sans-serif;color:var(--blue);padding-bottom:10px;border-bottom:2px solid #c7d5e5;white-space:nowrap;overflow:hidden}
.panel{left:99px;top:1593px;width:706px;height:276px;border:1px solid #e3e3e3}
.panel .list{position:absolute;left:0;top:0;width:267px;height:100%;border-right:1px solid #e3e3e3;padding:10px 0 0 12px;list-style:none}
.panel .list li{display:flex;align-items:center;gap:8px;font:400 12px "Open Sans",sans-serif;color:#555;height:32.5px;white-space:nowrap}
.panel .list li i{width:10px;height:10px;border-radius:50%;background:var(--blue);position:relative;flex:none}
.panel .list li i::after{content:"";position:absolute;left:3px;top:3px;border:2px solid transparent;border-left:3px solid #fff}
.marathon-art{left:285px;top:20px;width:232px;height:130px;background:linear-gradient(135deg,#c79a2c,#ecd07b)}
.marathon-title{left:533px;top:35px;font:400 26px/1.3 "Shadows Into Light Two",cursive;color:#333;width:160px}
.panel .body{position:absolute;left:285px;top:170px;width:405px;font-size:11px;line-height:2}
.panel .body a{color:var(--blue);font-style:italic;text-decoration:none}

/* sidebar */
.founders{left:836px;top:834px;width:265px;height:377px;background:#eef4fa}
.founders .photo{height:282px;background:linear-gradient(135deg,#cfd6dc,#8a8f95)}
.founders h3{text-align:center;font:700 14px "Open Sans",sans-serif;color:var(--navy);margin-top:18px}
.founders p{text-align:center;font:italic 400 11px/1.6 "Open Sans",sans-serif;color:#777;margin:6px 20px 0}
.novena{left:836px;top:1240px;width:265px;height:350px;border:1px solid #ddd;background:linear-gradient(180deg,#f1ece6,#ddd3c8)}
.rebuild{left:836px;top:1617px;width:265px;height:62px;background:linear-gradient(90deg,#7a1f13,#3a2a22)}
.side-quote{left:836px;top:1679px;width:265px;height:189px;background:#eef4fa;padding:14px 20px;font:italic 400 11px/2 "Open Sans",sans-serif;color:#4d84b4}

/* recent */
.recent{left:0;top:1900px;width:1200px;height:416px;background:var(--soft)}
.recent h2{position:absolute;left:99px;top:45px;font:700 16px "Raleway",sans-serif;color:#333}
.card{position:absolute;top:97px;width:320px}
.card .circle{width:145px;height:145px;border-radius:50%;border:5px solid #fff;box-shadow:0 0 0 1px #ddd}
.card h4{position:absolute;left:162px;top:42px;font:700 12px/2 "Raleway",sans-serif;color:#333}
.card .body{margin-top:25px;font-size:11px;line-height:1.9;color:#777}
.card .btn{margin-top:20px}
.sep{position:absolute;top:255px;width:1px;height:70px;background:#dfe5ea}

/* footer */
.footer{left:0;top:2316px;width:1200px;height:110px;background:var(--footer)}
.footer .fname{position:absolute;left:99px;top:30px;font:700 12px "Raleway",sans-serif;color:#cfcfcf;display:flex;align-items:center;gap:6px;white-space:nowrap}
.footer .fname b{width:14px;height:14px;background:#9a9a9a;flex:none}
.footer nav{position:absolute;left:262px;top:32px;font:500 12px "Raleway",sans-serif;color:#eee;letter-spacing:.3px;white-space:nowrap}
.footer nav span{margin:0 5px;color:#aaa}
.footer .copy{position:absolute;left:262px;top:58px;font:500 10px "Raleway",sans-serif;color:#aaa;letter-spacing:.3px;white-space:nowrap}
.footer .ring{position:absolute;top:32px;width:42px;height:42px;border-radius:50%;border:2px solid #999;display:flex;align-items:center;justify-content:center}
</style>
</head>
<body>

<header>
  <div class="brand abs">
    <div class="tagline">"...Rebuild My Church!"</div>
    <div class="name"><i class="mark"></i><span>Pinecrest Harborway</span></div>
    <div class="sub">Construyendo Familias</div>
    <div class="url">www.pinecrestharborway.org</div>
  </div>
  <div class="social abs">
    <div class="search"><svg width="13" height="13" viewBox="0 0 13 13"><circle cx="5.5" cy="5.5" r="4" fill="none" stroke="#0b3f80" stroke-width="2"/><line x1="8.5" y1="8.5" x2="12" y2="12" stroke="#0b3f80" stroke-width="2"/></svg></div>
    <span class="label">Connect with our social network</span>
    <i class="dot" style="background:#2f6eb5"></i>
    <i class="dot" style="background:#3fa6dd"></i>
    <i class="dot" style="background:#e8a11f"></i>
    <i class="dot" style="background:#1a73a8"></i>
  </div>
</header>

<nav class="nav abs">
  <a class="active" style="width:122px">HOME</a>
  <a style="width:116px">ABOUT US</a>
  <a style="width:170px">MINISTRY SERVICES</a>
  <a style="width:120px">EVENTS</a>
  <a style="width:100px">STORE</a>
  <a style="width:160px">RESOURCES</a>
  <a style="width:120px">CONTACT</a>
</nav>

<section class="hero abs" role="img" aria-label="White country church with tall steeple under a cloudy sky, green trees and lawn">
  <h1>Hey! I am first heading line<br>feel free to change me...</h1>
  <span class="arrow" style="left:32px"><svg width="12" height="12" viewBox="0 0 12 12"><path d="M8 1 3 6l5 5" fill="none" stroke="#fff" stroke-width="2"/></svg></span>
  <span class="arrow" style="right:32px"><svg width="12" height="12" viewBox="0 0 12 12"><path d="M4 1l5 5-5 5" fill="none" stroke="#fff" stroke-width="2"/></svg></span>
</section>
<div class="mission abs">"The future of the Church is being built in the Hearts &amp; Homes of today's Marriages &amp; Families. We believe we all must do EVERYTHING we can to support them!"<br>-Helen &amp; Mark</div>

<main>
  <h2 class="h2 abs" style="left:99px;top:830px">WELCOME TO PINECREST HARBORWAY!</h2>
  <div class="welcome-img abs" role="img" aria-label="Ministry poster: a great marriage, some wish for it, we work for it"></div>
  <p class="body abs" style="left:422px;top:880px;width:383px">What if intensify our efforts, one Parish/Cluster at a time, to Heal Hearts, Renew Marriages, Challenge Singles, Strengthen Families and Evangelize Parishes, all under the Mantle of Our Lady of Guadalupe? We can call it... What if we start by taking the...</p>
  <p class="body abs" style="left:422px;top:980px;width:383px">Message of the Gospel, illuminating it by the witness of dynamic marriage evangelists who are rising up amongst us, add spirited music and moving technology, and invite Married Couples...</p>
  <a class="btn abs" style="left:424px;top:1060px">Read More</a>
  <div class="rule abs" style="left:99px;top:1137px;width:706px"></div>

  <h2 class="h2 abs" style="left:99px;top:1170px">PINECREST HARBORWAY REVOLUTION!</h2>
  <blockquote class="quote abs">"Today, there are those who say that marriage is out of fashion. They say that it is not worth making a lifelong commitment, making a definitive decision, 'forever', because we do not know what tomorrow will bring. I ask you, instead, to be revolutionaries." Bishop Tomas Arvelo's address to Youth Gathering Volunteers, Lisbon (July 28, 2013)
    <span class="pager"><i></i><i></i></span>
  </blockquote>
  <div class="badge abs" style="left:99px"><b style="background:#f3e4e6"></b></div>
  <div class="badge abs" style="left:341px"><b style="background:#d8e6e8"></b></div>
  <div class="badge abs" style="left:583px"><b style="background:#e9e2cc"></b></div>

  <div class="lead abs">A dynamic, innovative and effective way to create on-going relational and spiritual support for...</div>
  <div class="panel abs">
    <ul class="list">
      <li><i></i>Dating Individuals &amp; Couples</li>
      <li><i></i>Engaged and Newly Married Couples</li>
      <li><i></i>Early Married Couples</li>
      <li><i></i>Convalidating &amp; Remarriage Couples</li>
      <li><i></i>Struggling couples</li>
      <li><i></i>Military Couples</li>
      <li><i></i>Widows and Widowers</li>
      <li><i></i>Parish Harborway Ministry Teams</li>
    </ul>
    <div class="marathon-art abs" role="img" aria-label="Gold lettered artwork: to strengthen and to sanctify"></div>
    <div class="marathon-title abs">Harborway Marathon!</div>
    <p class="body">What if we start by taking the Message of the Gospel, illuminating it bywitness of dynamic marriage evangelists who are rising up amongst us, add spirited music and moving technology, and invite Married Couples, Singles, and the Clergy by the bus loads (or at least the car loads) to join... <a>Read More</a></p>
  </div>
</main>

<aside>
  <div class="founders abs">
    <div class="photo" role="img" aria-label="Portrait of the ministry founders, a smiling married couple"></div>
    <h3>Helen &amp; Mark Ostrander</h3>
    <p>Founders, Pinecrest Harborway, Catholic Marriage-Building Specialists</p>
  </div>
  <div class="novena abs" role="img" aria-label="Novena booklet cover with clasped hands, taking us to prayer"></div>
  <div class="rebuild abs" role="img" aria-label="Banner for rebuilding your life after divorce"></div>
  <div class="side-quote abs">"St. Francis set out to Renew the Church..it's still the work before us today, but when we knelt before the cross of San Damiano in Assisi, the Lord reminded us that now it's Marriages and Families that are in the need of rebuilding. It is this rebuilding that will bring renewal to the Church today!"</div>
</aside>

<section class="recent abs">
  <h2>RECENT UPDATES</h2>
  <article class="card" style="left:99px">
    <div class="circle" role="img" aria-label="Devotional painting of the Virgin Mary" style="background:linear-gradient(135deg,#7a5b6e,#2e2a3c)"></div>
    <h4>HARBOR MANTLE, a Parish<br>Ministry for Brides<br>&amp; Grooms</h4>
    <p class="body">Sed ut perspiciatis unde omnis iste natus error sit voluptat tium doloremque laudantium, totam rem aperiam, eaque ipsa quae ab illo inventore veritatis...</p>
    <a class="btn">Read More</a>
  </article>
  <i class="sep" style="left:430px"></i>
  <article class="card" style="left:448px">
    <div class="circle" role="img" aria-label="Devotional image of Our Lady of Guadalupe" style="background:linear-gradient(135deg,#c78a3a,#4a6e4c)"></div>
    <h4>Parish HARBORCARE<br>for Couples in Crisis</h4>
    <p class="body">Sed ut perspiciatis unde omnis iste natus error sit voluptat tium doloremque laudantium, totam rem aperiam, eaque ipsa quae ab illo inventore veritatis...</p>
    <a class="btn">Read More</a>
  </article>
  <i class="sep" style="left:780px"></i>
  <article class="card" style="left:797px">
    <div class="circle" role="img" aria-label="Two framed devotional images of the Sacred Heart and Immaculate Heart" style="background:linear-gradient(135deg,#f1e2bd,#e6cf98)"></div>
    <h4>Evangelizing Families &amp;<br>Households--Consecra<br>tion to Sacred Heart &amp;<br>Immaculate Heart</h4>
    <p class="body">Sed ut perspiciatis unde omnis iste natus error sit voluptat tium doloremque laudantium, totam rem aperiam, eaque ipsa quae ab illo inventore veritatis...</p>
    <a class="btn">Read More</a>
  </article>
</section>

<footer class="footer abs">
  <div class="fname"><b></b>Pinecrest Harborway</div>
  <nav>HOME<span>|</span>ABOUT US<span>|</span>MINISTRY SERVICES<span>|</span>EVENTS<span>|</span>STORE<span>|</span>RESOURCES<span>|</span>CONTACT</nav>
  <div class="copy">COPYRIGHTS©PINECRESTHARBORWAY.ORG 2016 | ALLRIGHTS RESERVED</div>
  <span class="ring" style="left:1006px"><svg width="18" height="14" viewBox="0 0 18 14"><rect x="1" y="1" width="16" height="12" fill="none" stroke="#ccc" stroke-width="1.6"/><path d="M1 1l8 7 8-7" fill="none" stroke="#ccc" stroke-width="1.6"/></svg></span>
  <span class="ring" style="left:1058px"><svg width="14" height="14" viewBox="0 0 14 14"><path d="M7 12V2M2 7l5-5 5 5" fill="none" stroke="#ccc" stroke-width="2"/></svg></span>
</footer>

</body>
</html>
```